Business / Discount Card

Looking to create a 2 sided business card. Front side to say "Thanks for flying with Skyward Drifts" then have link to "In-Flight Photos, www.skywarddrifts-example.com.au, password: skyward" Back side of card to have company logo, phone number, facebook & instagram logo and #skywarddrifts. Also included on this side will be discount text "Book again and save 10%. Use discount code: skyward10"Round Corner Card Templates are attached. Please ensure dimensions are correct.Thanks,

Font styles to use
Sans Serif

Colors
33a6d7
ffffff
000000

Requirements
Must have
• Logo
• Blue, White and Black color scheme

```html
<!DOCTYPE html>
<html lang="en">
<head>
<meta charset="utf-8">
<title>Skyward Drifts – Discount Card</title>
<link rel="stylesheet" href="https://fonts.googleapis.com/css2?family=Exo+2:ital,wght@1,600&family=Lato:ital,wght@0,400;0,700;1,400;1,700&display=swap">
<style>
  :root {
    --sky-blue: #33a6d7;
    --ink: #000000;
    --card-black: #040608;
    --paper: #ffffff;
    --stage: #2a2a2a;
    --text-dark: #1a1a1a;
  }
  * { margin: 0; padding: 0; box-sizing: border-box; }
  html, body {
    width: 1200px; height: 1200px; overflow: hidden;
    background: var(--stage);
    font-family: "Lato", sans-serif;
  }
  .card {
    position: absolute;
    left: 198px;
    width: 804px;
    height: 510px;
    border-radius: 32px;
    overflow: hidden;
  }
  .card-front { top: 66px; background: var(--card-black); }
  .card-back { top: 610px; background: var(--paper); }

  .thanks-line {
    position: absolute; left: 0; right: 0; top: 212px;
    text-align: center;
    font-family: "Exo 2", sans-serif;
    font-style: italic; font-weight: 600;
    font-size: 27px; letter-spacing: 1.5px;
    color: var(--sky-blue);
  }
  .photos-info {
    position: absolute; left: 0; right: 0; top: 434px;
    text-align: center; color: var(--paper);
    font-size: 20px; line-height: 25px; letter-spacing: 0.6px;
  }
  .photos-info .accent { color: var(--sky-blue); }
  .photos-info .password { color: var(--sky-blue); font-style: italic; font-weight: 700; }

  .brand-name {
    position: absolute; left: 0; right: 0; top: 118px;
    text-align: center;
    font-size: 54px; font-weight: 700; letter-spacing: 1px;
    color: var(--ink);
  }

  .contact {
    position: absolute; left: 28px;
    display: flex; align-items: center; gap: 12px;
    font-size: 20px; letter-spacing: 1px; color: var(--text-dark);
  }
  .contact-phone { top: 390px; }
  .contact-social { top: 430px; }
  .contact svg { width: 20px; height: 20px; }
  .social-square { width: 18px; height: 18px; border-radius: 3px; background: var(--sky-blue); }

  .offer {
    position: absolute; left: 493px;
    font-size: 20px; letter-spacing: 0.8px; color: var(--text-dark);
  }
  .offer-save { top: 397px; }
  .offer-code { top: 434px; }
  .offer .highlight { color: var(--sky-blue); font-style: italic; }

  .bottom-band { position: absolute; left: 0; bottom: 0; width: 804px; height: 28px; }
</style>
</head>
<body>
  <section class="card card-front">
    <p class="thanks-line">Thanks for flying with Skyward Drifts</p>
    <div class="photos-info">
      <p>In-Flight Photos</p>
      <p>www.<span class="accent">skywarddrifts-example</span>.com.au, password: <span class="password">skyward</span></p>
    </div>
  </section>

  <section class="card card-back">
    <h1 class="brand-name">Skyward Drifts</h1>

    <div class="contact contact-phone">
      <svg viewBox="0 0 24 24" aria-hidden="true">
        <path fill="#33a6d7" d="M6.6 10.8a15 15 0 0 0 6.6 6.6l2.2-2.2c.3-.3.7-.4 1-.2 1.1.4 2.3.6 3.6.6.6 0 1 .4 1 1V20c0 .6-.4 1-1 1A17 17 0 0 1 3 4c0-.6.4-1 1-1h3.5c.6 0 1 .4 1 1 0 1.3.2 2.5.6 3.6.1.3 0 .7-.2 1z"/>
      </svg>
      <span>123 456 7890</span>
    </div>
    <div class="contact contact-social">
      <span class="social-square"></span>
      <span>#skywarddrifts</span>
    </div>

    <p class="offer offer-save">Book again and save <span class="highlight">10%</span></p>
    <p class="offer offer-code">Use discount code: <span class="highlight">skyward10</span></p>

    <svg class="bottom-band" viewBox="0 0 804 28" aria-hidden="true">
      <polygon points="0,0 410,0 382,28 0,28" fill="#040608"/>
      <polygon points="412,0 804,0 804,28 384,28" fill="#29abe2"/>
    </svg>
  </section>
</body>
</html>
```